A 1 to 2 page digital flyer, using my existing logo and branding files.

I need a professional1 to 2 page flyer in both digital file and an editable PDF form to advertise service offerings for my coaching and consulting business.
The flyer should be upmarket, professional and conservative in style to meet the expectations of my professional market (doctors, psychologists and executives).
It will be based on my existing logo and brand, see my current website: www.harlowmentoring.com
Here are the key elements needed:
1) First the main product offering (which I should be able to edit myself for future use). In this first case, this features an advertisement for a 'Therapy group for professionals'. (see attached file).
2) The second key text is my bio/profile which includes a photo.
3) The third section is a call to action, including my contact details.
4) The flyer should include my email, website and phone contact details.
5) It should also include some small logos of my professional accrediting organisations.

Target Market(s)

Doctors, psychologists, executives in healthcare.

Industry/Entity Type

Health care and business schools

Font styles to use
Other font styles liked:
• Operetta (headings), Sofia Pro (body text).

Colors
0054AA
0677BA
7BADD7
CADEEF
E8F1F8

Requirements
Must have
• 1. Strong adherence to my brand voice and design elements, as featured on my website and in my branded stationery. 2. Editable text sections in PDF that I can re-use for future advertisements. 3. Suitable size and medium (e.g. A4 size) for sharing digitally via my website, email, and social media. 4) Very prompt design as soon as possible please - quick turnaround will secure the winning place.
Nice to have
• Please use design images and inspiration from my website. An additional stock photo of a therapy group is uploaded as an example
Should not have
• Do not deviate from my brand voice, fonts and colours please.

```html
<!DOCTYPE html>
<html lang="en">
<head>
<meta charset="utf-8">
<title>Harlow Mentoring – Flyer</title>
<link rel="stylesheet" href="https://fonts.googleapis.com/css2?family=Cormorant+Garamond:wght@500&family=Jost:wght@400;500;600&display=swap">
<style>
  :root{
    --brand-deep:#0054AA;
    --brand-mid:#0677BA;
    --brand-block:#3a6bb8;
    --brand-soft:#7BADD7;
    --brand-pale:#CADEEF;
    --brand-mist:#E8F1F8;
    --ink:#1c2233;
    --white:#ffffff;
  }
  *{margin:0;padding:0;box-sizing:border-box}
  html,body{width:848px;height:1200px;overflow:hidden;background:#fff}
  .flyer{position:relative;width:848px;height:1200px;background:var(--white);font-family:"Jost",sans-serif;color:var(--ink);overflow:hidden}

  .hero{position:absolute;left:0;top:0;width:848px;height:405px}
  .hero-photo{position:absolute;inset:0;background:
      radial-gradient(ellipse at 30% 30%, rgba(150,170,210,.55), transparent 60%),
      linear-gradient(160deg,#5a6f9c 0%,#34457a 45%,#2a3763 75%,#4c5c8c 100%)}
  .hero-site{position:absolute;left:238px;top:52px;color:var(--white);font-size:15px;letter-spacing:.2px}
  .hero-badge{position:absolute;left:660px;top:38px;width:112px;height:112px;border-radius:50%;background:var(--brand-block);color:var(--white);font-size:17px;line-height:20px;text-transform:uppercase;display:flex;align-items:center;justify-content:center;text-align:center;letter-spacing:.5px}
  .hero-title{position:absolute;left:60px;top:150px;width:740px;color:var(--white);font-family:"Cormorant Garamond",serif;font-weight:500;font-size:66px;line-height:64px;text-align:center}
  .hero-rule{position:absolute;left:210px;top:288px;width:380px;height:2px;background:var(--brand-mid)}

  .profile-block{position:absolute;left:22px;top:405px;width:250px;height:470px;background:var(--brand-block)}
  .profile-photo{position:absolute;left:22px;top:432px;width:222px;height:422px;background:
      linear-gradient(180deg,#7a9f6a 0%,#5c7f58 30%,#2e4a7f 60%,#243d72 100%)}

  .ripple-photo{position:absolute;left:272px;top:560px;width:576px;height:400px;background:
      radial-gradient(ellipse at 52% 52%, rgba(255,255,255,.9) 0%, rgba(200,210,228,.6) 30%, transparent 55%),
      linear-gradient(180deg,#ffffff 0%,#dfe5ef 30%,#9aa9c4 70%,#7f90b2 100%)}
  .ripple-wedge{position:absolute;left:0;top:0;width:848px;height:1200px;pointer-events:none}

  .bio{position:absolute;left:292px;top:418px;width:520px}
  .bio-name{font-size:21px;font-weight:600;line-height:25px;color:var(--ink);margin-bottom:10px}
  .bio p{font-size:11.5px;line-height:14.5px;margin-bottom:10px}
  .contact{position:absolute;left:292px;top:668px;width:520px;text-align:center;color:var(--brand-deep);font-weight:600;font-size:14px}
  .contact div{margin-bottom:20px}

  .footer{position:absolute;left:0;top:960px;width:848px;height:240px;background:var(--white)}
  .brand{position:absolute;left:62px;top:72px;display:flex;align-items:center;gap:18px}
  .brand-mark{width:40px;height:40px;background:var(--brand-block)}
  .brand-name{font-family:"Cormorant Garamond",serif;font-weight:500;font-size:40px;line-height:36px;color:var(--brand-block)}
  .accredit{position:absolute;left:512px;top:40px}
  .accredit-label{font-size:11px;color:var(--brand-deep);margin-bottom:10px}
  .accredit-badges{display:flex;gap:18px;align-items:center}
  .badge-round{width:40px;height:40px;border-radius:50%;background:var(--brand-pale);border:3px solid var(--brand-deep)}
  .badge-rect{width:64px;height:30px;background:var(--brand-mist);border:2px solid var(--brand-mid)}
  .badge-tag{width:62px;height:28px;background:#6a4e9a}
</style>
</head>
<body>
<main class="flyer">
  <section class="hero">
    <div class="hero-photo" role="img" aria-label="Photo of a therapy group of professionals seated in a circle, in cool blue tones"></div>
    <div class="hero-site">www.harlowmentoring.com</div>
    <div class="hero-badge">Book<br>Online<br>Today</div>
    <h1 class="hero-title">Are you ready to create<br>meaningful change?</h1>
    <div class="hero-rule"></div>
  </section>

  <div class="ripple-photo" role="img" aria-label="Photo of a water droplet making ripples on a calm surface"></div>
  <svg class="ripple-wedge" viewBox="0 0 848 1200" aria-hidden="true">
    <polygon points="272,700 272,960 560,830" fill="#3a6bb8" opacity=".35"/>
  </svg>

  <div class="profile-block"></div>
  <div class="profile-photo" role="img" aria-label="Portrait photo of Daniel Harlow in a blue blazer outdoors"></div>

  <section class="bio">
    <h2 class="bio-name">Daniel Harlow – Professor of Organisational Culture and Leadership</h2>
    <p>Daniel is a specialist in the deep personal change that professionals need in their lives and work. He works with professionals and leaders across private, public and government organisations, helping them catalyse personal and cultural change.</p>
    <p>In his work as a professor at Northgate University, Kingsbridge College and Southbank University, he has developed specialist expertise in creating cultural change, particularly in healthcare. He is an accredited psychoanalytic psychotherapist, group analyst and certified executive coach.</p>
    <p>Before his business-school career, he was a public health clinical director and lead consultant psychotherapist. He worked in major teaching hospitals in Manchester, Liverpool and London. He holds a PhD in organisational culture and leadership from Regent College, Westmoor University.</p>
  </section>

  <section class="contact">
    <div>For Further Information Call: +61 3 9000 4120</div>
    <div>Email: info@harlowmentoring.com</div>
  </section>

  <footer class="footer">
    <div class="brand">
      <div class="brand-mark"></div>
      <div class="brand-name">Harlow<br>Mentoring</div>
    </div>
    <div class="accredit">
      <div class="accredit-label">Our Accrediting Organisations</div>
      <div class="accredit-badges">
        <div class="badge-round"></div>
        <div class="badge-rect"></div>
        <div class="badge-tag"></div>
      </div>
    </div>
  </footer>
</main>
</body>
</html>
```